Conference Exhibit Poster/Banner for BrightwayFares.org

I need a poster/banner display designed for an upcoming trade show where we will be a sponsor/exhibitor.
Using our current website, logos, pictures, color scheme, please design a banner that will emphasize our main business: Brightway Fares and our missionary/group airfare specialties, while also incorporating our "Vacations" and "Holy Land" division services. I would like this mostly large graphic/font/logo focused and less text overall.
BrightwayFares.org is a full-service online travel agency specializing in international individual & group airfare. Mostly serving missions/church/volunteer teams, we help make travel arrangements for thousands each year who serve and help people around the world.
Recently, we also opened "Vacations" and "Holy Land" divisions to offer a full-service travel agency element. We can help people arrange any type of travel they need.
Please see this link for the actual dimensions and art specifications needed for the final product (a retractable banner display):
http://www.pellumdisplays.com/catalog/product/view/id/1412/s/otter-36/?container=1195&container=1195
Print Layout Size: 36"w x 94"h
Safe Viewable Zone: 36"w x 89"h
SEE MORE info by downloading the .eps or .pdf files on this page above under "download" tab.
Target Market(s)
main target market is the Christian/faith/religious community. Mostly younger male youth pastor types in their 20s who help lead mission trips..
Industry/Entity Type
Travel
Requirements
Must have
- At minimum, our main Brightway Fares logo is a must - see uploaded file and our www.BrightwayFares.org
Ideally, the other logos can be incorporated too.
MUST have our name & website.
Nice to have
- MUST have our main homepage idea of who we are in the top, main section of poster banner. Group missionary airfare experts or something along those lines.
Nice to have the main picture of the kids as we need some picture/photo elements to the banner.
Nice to have a picture from the vacation site too advertising our vacation services (same for the Holy Land).

```html
<!DOCTYPE html>
<html lang="en">
<head>
<meta charset="utf-8">
<title>Brightway Fares – Exhibit Banner Concepts</title>
<link href="https://fonts.googleapis.com/css2?family=Cinzel:wght@700&family=Marcellus&display=swap" rel="stylesheet">
<style>
  :root{
    --page:#ffffff;
    --sand-light:#f4f1ec;
    --sand:#c9bba4;
    --gold:#eea83a;
    --gold-deep:#d98e20;
    --brown:#6b4a1f;
    --brown-dark:#5a3e1b;
    --ink:#3b2710;
    --teal:#19a9b4;
    --teal-dark:#12929c;
    --teal-light:#e8f6f7;
    --navy:#2b3a8c;
    --orange:#f29a2e;
    --photo-a:#c98a58;
    --photo-b:#5b3a26;
  }
  *{box-sizing:border-box;margin:0;padding:0}
  html,body{width:1200px;height:900px;overflow:hidden;background:var(--page)}
  .stage{position:relative;width:1200px;height:900px}
  .banner{position:absolute;overflow:hidden;box-shadow:4px 6px 10px rgba(0,0,0,.35)}
  .banner--earth{left:110px;top:80px;width:300px;height:705px;
    background:linear-gradient(90deg,var(--sand-light) 0%,#e6ddd0 55%,var(--sand) 100%)}
  .banner--sea{left:705px;top:70px;width:285px;height:700px;
    background:linear-gradient(90deg,#ffffff 0%,var(--teal-light) 35%,#7fd0d6 60%,var(--teal) 80%)}
  .swoosh{position:absolute;inset:0;width:100%;height:100%}
  .headline{position:absolute;font-family:"Cinzel",serif;font-weight:700;white-space:nowrap}
  .banner--earth .headline{color:var(--gold);text-shadow:1px 1px 0 var(--brown-dark)}
  .banner--sea .headline{color:var(--navy);text-shadow:1px 1px 0 #fff}
  .headline--vision{left:44px;top:10px;font-size:19px}
  .headline--mission{right:22px;font-size:19px}
  .banner--earth .headline--mission{top:405px}
  .banner--sea .headline--mission{top:385px}
  .photo{position:absolute;border-radius:50%;
    background:radial-gradient(circle at 40% 35%,var(--photo-a),var(--photo-b))}
  .banner--earth .photo{width:100px;height:100px;border:3px solid var(--gold)}
  .banner--sea .photo{width:102px;height:102px;border:3px solid #fff}
  .photo--chapel{background:linear-gradient(180deg,#e2b58e,#8c6d73 60%,#f0ece8)}
  .photo--kids{background:radial-gradient(circle at 50% 55%,#7a4a2c,#3a241a)}
  .photo--diver{background:radial-gradient(circle at 45% 40%,#c98a6a,#6f5a52)}
  .intro{position:absolute;left:0;right:0;font-family:"Marcellus",serif;color:var(--ink);
    background:rgba(255,255,255,.55);padding:8px 10px 8px 18px;line-height:1.22}
  .banner--earth .intro{top:430px;height:110px;font-size:20px}
  .banner--sea .intro{top:418px;height:110px;font-size:19px;color:#1e1e1e;background:rgba(255,255,255,.6)}
  .services{position:absolute;left:0;right:0;display:flex;justify-content:space-around;
    font-family:"Cinzel",serif;font-weight:700;font-size:12px}
  .banner--earth .services{top:548px;color:var(--gold);text-shadow:1px 1px 0 var(--brown-dark)}
  .banner--sea .services{top:540px;color:var(--navy);background:rgba(255,255,255,.55);padding:3px 0}
  .brands{position:absolute;left:0;right:0;display:flex;justify-content:space-around;align-items:center}
  .banner--earth .brands{top:568px}
  .banner--sea .brands{top:566px;background:#fff;height:34px;padding:0 4px}
  .brand{font-family:"Marcellus",serif;color:var(--brown-dark);text-align:center;line-height:1}
  .banner--earth .brand{width:52px;height:52px;border-radius:50%;background:#fff;
    border:2px solid var(--gold);display:flex;align-items:center;justify-content:center;font-size:9px}
  .banner--sea .brand{font-size:10px}
  .footer{position:absolute;left:0;right:0;bottom:0;display:flex;align-items:center;justify-content:center;
    font-family:"Marcellus",serif;font-weight:700}
  .banner--earth .footer{height:78px;background:var(--brown-dark);color:var(--sand-light);font-size:24px}
  .banner--sea .footer{height:95px;background:var(--teal);color:var(--orange);font-size:21px;
    text-shadow:1px 1px 0 #7a4a12;padding-bottom:20px}
</style>
</head>
<body>
<main class="stage">

  <section class="banner banner--earth" aria-label="Brightway Fares banner, earth tones">
    <svg class="swoosh" viewBox="0 0 300 705" preserveAspectRatio="none" aria-hidden="true">
      <path d="M70 120 C150 220 140 330 100 420 C80 470 70 520 70 630 L0 630 L0 300 C40 260 60 200 70 120 Z" fill="var(--brown)"/>
      <path d="M40 0 C90 80 150 170 135 280 C120 380 60 440 70 630" fill="none" stroke="var(--gold)" stroke-width="12"/>
      <path d="M0 0 L40 0 C70 50 60 80 40 95 Z" fill="var(--gold)"/>
    </svg>
    <h2 class="headline headline--vision">Your VISION...</h2>
    <div class="photo photo--chapel" style="left:95px;top:45px" role="img" aria-label="Whitewashed chapel bell tower at sunset over the sea"></div>
    <div class="photo photo--kids" style="left:137px;top:152px" role="img" aria-label="Group of smiling children on a mission trip"></div>
    <div class="photo photo--diver" style="left:125px;top:275px" role="img" aria-label="Vacationer with snorkel mask at the beach"></div>
    <h2 class="headline headline--mission">...is Our MISSION</h2>
    <p class="intro">If you need to get to the mission field, would like to visit the holy land or simply get away... we can help</p>
    <div class="services"><span>Mission Trips</span><span>Israel Tours</span><span>Vacations</span></div>
    <div class="brands">
      <span class="brand">Brightway Fares</span>
      <span class="brand">Brightway Fares</span>
      <span class="brand">Brightway Fares</span>
    </div>
    <div class="footer">www.BrightwayFares.org</div>
  </section>

  <section class="banner banner--sea" aria-label="Brightway Fares banner, ocean tones">
    <svg class="swoosh" viewBox="0 0 285 700" preserveAspectRatio="none" aria-hidden="true">
      <path d="M55 0 C110 80 130 200 115 300 C100 400 70 480 95 620 L285 620 L285 0 Z" fill="var(--teal-dark)" opacity=".85"/>
      <path d="M20 0 C80 90 100 200 90 300 C80 420 50 500 120 620" fill="none" stroke="#fff" stroke-width="2"/>
    </svg>
    <h2 class="headline headline--vision" style="left:8px">Your VISION...</h2>
    <div class="photo photo--chapel" style="left:62px;top:40px" role="img" aria-label="Whitewashed chapel bell tower at sunset over the sea"></div>
    <div class="photo photo--kids" style="left:115px;top:145px" role="img" aria-label="Group of smiling children on a mission trip"></div>
    <div class="photo photo--diver" style="left:115px;top:265px" role="img" aria-label="Vacationer with snorkel mask at the beach"></div>
    <h2 class="headline headline--mission">...is Our MISSION</h2>
    <p class="intro">If you need to get to the mission field, would like to visit the holy land or simply get away... we can help</p>
    <div class="services"><span>Mission Trips</span><span>Israel Tours</span><span>Vacations</span></div>
    <div class="brands">
      <span class="brand">Brightway Fares</span>
      <span class="brand">Brightway Fares</span>
      <span class="brand">Brightway Fares</span>
    </div>
    <div class="footer">www.BrightwayFares.org</div>
  </section>

</main>
</body>
</html>
```